Brenwick Structures Construction Company Seeking Modern Website

We are a small construction company wanting to create a web presence. We don't have much in the way of current content but will get photos as they come in. Attached is a picture of our business card.
The pages we would like on the menu are:
Home
Portfolio
Product Specs
Testimonials
Our Process
Contact
Some designs we like are:
http://www.tovandrafters.example/
http://www.qrkframes.example/
http://harnestshed.example/
http://pellowbarns.example/
Not much requirements other than that so feel free to be creative!
Target Market(s)
Construction
Commercial and Residential Buildings
Industry/Entity Type
Construction Company
Number of Pages Required
5+ page

```html
<!DOCTYPE html>
<html lang="en">
<head>
<meta charset="utf-8">
<title>Brenwick Structures — Home</title>
<link rel="stylesheet" href="https://fonts.googleapis.com/css2?family=Inter:wght@700;800&family=Raleway:wght@200;300&display=swap">
<style>
  :root {
    --brand-yellow: #fdc52a;
    --panel-yellow: rgba(253, 197, 42, 0.78);
    --nav-black: #181818;
    --page-white: #ffffff;
    --text-white: #ffffff;
    --photo-dark: #1c1c1c;
    --photo-mid: #6a6a6a;
    --photo-light: #c9c9c9;
  }
  html, body {
    margin: 0;
    padding: 0;
    width: 1200px;
    height: 880px;
    overflow: hidden;
    background: var(--page-white);
  }
  .canvas {
    position: relative;
    width: 1200px;
    height: 880px;
    background: var(--page-white);
    overflow: hidden;
  }
  .accent-band {
    position: absolute;
    left: 0; top: 33px;
    width: 1200px; height: 16px;
    background: var(--brand-yellow);
  }
  .site-nav {
    position: absolute;
    left: 0; top: 49px;
    width: 1200px; height: 103px;
    background: var(--nav-black);
  }
  .nav-art {
    position: absolute;
    left: 0; top: 0;
    width: 1200px; height: 103px;
  }
  .brand-name {
    font-family: "Inter", Arial, sans-serif;
    font-weight: 700;
    font-size: 30px;
    fill: var(--text-white);
  }
  .current-tab { fill: var(--brand-yellow); }
  .nav-label {
    font-family: "Raleway", Arial, sans-serif;
    font-weight: 200;
    font-size: 30px;
    fill: var(--text-white);
  }
  .nav-label.is-current { fill: var(--nav-black); font-weight: 300; }
  .nav-label.is-contact { fill: var(--brand-yellow); }
  .hero-photo {
    position: absolute;
    left: 0; top: 152px;
    width: 1200px; height: 680px;
    background:
      radial-gradient(ellipse at 72% 55%, var(--photo-mid) 0%, rgba(40,40,40,0.6) 40%, transparent 70%),
      linear-gradient(100deg, var(--photo-light) 0%, var(--photo-mid) 30%, var(--photo-dark) 60%, #3a3a3a 85%, var(--photo-dark) 100%);
  }
  .info-panel {
    position: absolute;
    left: 40px; top: 188px;
    width: 516px; height: 532px;
    border-radius: 64px;
    background: var(--panel-yellow);
  }
  .hero-text {
    position: absolute;
    left: 0; top: 0;
    width: 1200px; height: 880px;
  }
  .info-line {
    font-family: "Raleway", Arial, sans-serif;
    font-weight: 300;
    font-size: 19px;
    fill: var(--text-white);
  }
  .headline-line {
    font-family: "Inter", Arial, sans-serif;
    font-weight: 800;
    fill: var(--brand-yellow);
    letter-spacing: -2px;
  }
  .headline-line.size-main { font-size: 60px; }
  .headline-line.size-you { font-size: 106px; }
  .headline-line.size-memories { font-size: 82px; }
</style>
</head>
<body>
<div class="canvas">
  <div class="accent-band"></div>

  <header class="site-nav">
    <svg class="nav-art" viewBox="0 0 1200 103" aria-label="Site navigation">
      <text class="brand-name" x="14" y="63" textLength="242" lengthAdjust="spacingAndGlyphs">Brenwick Structures</text>
      <rect class="current-tab" x="266" y="0" width="89" height="100"/>
      <text class="nav-label is-current" x="274" y="60" textLength="77" lengthAdjust="spacingAndGlyphs">HOME</text>
      <text class="nav-label" x="376" y="63" textLength="124" lengthAdjust="spacingAndGlyphs">PORTFOLIO</text>
      <text class="nav-label" x="524" y="63" textLength="176" lengthAdjust="spacingAndGlyphs">PRODUCT SPECS</text>
      <text class="nav-label" x="724" y="63" textLength="154" lengthAdjust="spacingAndGlyphs">TESTIMONIALS</text>
      <text class="nav-label" x="902" y="63" textLength="152" lengthAdjust="spacingAndGlyphs">OUR PROCESS</text>
      <text class="nav-label is-contact" x="1075" y="63" textLength="103" lengthAdjust="spacingAndGlyphs">CONTACT</text>
    </svg>
  </header>

  <div class="hero-photo" role="img" aria-label="Black and white photo of a construction worker in a hard hat climbing a caged steel stairway inside a building under construction"></div>

  <div class="info-panel"></div>

  <svg class="hero-text" viewBox="0 0 1200 880">
    <g class="info-block">
      <text class="info-line" x="106" y="222" textLength="400" lengthAdjust="spacingAndGlyphs">INFORMATION GOES HERE INFORMATION GOES HERE</text>
      <text class="info-line" x="106" y="266" textLength="400" lengthAdjust="spacingAndGlyphs">INFORMATION GOES HERE INFORMATION GOES HERE</text>
      <text class="info-line" x="106" y="309" textLength="400" lengthAdjust="spacingAndGlyphs">INFORMATION GOES HERE INFORMATION GOES HERE</text>
      <text class="info-line" x="106" y="353" textLength="400" lengthAdjust="spacingAndGlyphs">INFORMATION GOES HERE INFORMATION GOES HERE</text>
      <text class="info-line" x="106" y="397" textLength="400" lengthAdjust="spacingAndGlyphs">INFORMATION GOES HERE INFORMATION GOES HERE</text>
      <text class="info-line" x="106" y="441" textLength="400" lengthAdjust="spacingAndGlyphs">INFORMATION GOES HERE INFORMATION GOES HERE</text>
      <text class="info-line" x="106" y="484" textLength="400" lengthAdjust="spacingAndGlyphs">INFORMATION GOES HERE INFORMATION GOES HERE</text>
      <text class="info-line" x="106" y="528" textLength="400" lengthAdjust="spacingAndGlyphs">INFORMATION GOES HERE INFORMATION GOES HERE</text>
      <text class="info-line" x="106" y="572" textLength="400" lengthAdjust="spacingAndGlyphs">INFORMATION GOES HERE INFORMATION GOES HERE</text>
      <text class="info-line" x="106" y="616" textLength="400" lengthAdjust="spacingAndGlyphs">INFORMATION GOES HERE INFORMATION GOES HERE</text>
      <text class="info-line" x="106" y="659" textLength="400" lengthAdjust="spacingAndGlyphs">INFORMATION GOES HERE INFORMATION GOES HERE</text>
      <text class="info-line" x="106" y="703" textLength="400" lengthAdjust="spacingAndGlyphs">INFORMATION GOES HERE INFORMATION GOES HERE</text>
    </g>

    <g class="hero-headline">
      <text class="headline-line size-main" x="624" y="254" textLength="508" lengthAdjust="spacingAndGlyphs">Building dreams, so</text>
      <text class="headline-line size-you" x="732" y="332" textLength="184" lengthAdjust="spacingAndGlyphs">you</text>
      <text class="headline-line size-main" x="932" y="332" textLength="236" lengthAdjust="spacingAndGlyphs">can build</text>
      <text class="headline-line size-memories" x="784" y="408" textLength="372" lengthAdjust="spacingAndGlyphs">memories</text>
    </g>
  </svg>
</div>
</body>
</html>
```